VORN - Business cards

Business card to be created for Commercial sales staff

Target Market(s)

Commercial businesses

Industry/Entity Type

Commercial

Contact Information for Business Card

Look professional. For commercial clients

Colors
ffffff

Requirements
Must have
• - Vorn Logo
• - Commercial sales staff as postion
• - room for commerical sales manager role
• - person name and their mobile number
• - Website : vornelectrical.com.au
Nice to have
• White background.
• On back of business card just have the logo no other information
Should not have
• Should only have white background on front of card.

```html
<!DOCTYPE html>
<html lang="en">
<head>
<meta charset="utf-8">
<title>VORN – Business Cards</title>
<link rel="stylesheet" href="https://fonts.googleapis.com/css2?family=Roboto:wght@400;500;900&display=swap">
<style>
  :root {
    --stage: #2b2c30;
    --card-dark: #3b3e46;
    --paper: #ffffff;
    --brand-red: #c8101a;
    --brand-red-deep: #a50b13;
    --ink: #3a3d45;
    --on-dark: #ffffff;
    --on-dark-soft: #d5d7dc;
  }
  html, body {
    margin: 0;
    width: 1200px;
    height: 950px;
    overflow: hidden;
    background: radial-gradient(circle at 50% 45%, #4a4b50 0%, var(--stage) 70%);
    font-family: "Roboto", Arial, sans-serif;
  }
  .card {
    position: absolute;
    width: 620px;
    height: 354px;
    overflow: hidden;
    box-shadow: 0 18px 40px rgba(0,0,0,.45);
  }
  /* Back of card */
  .card--back {
    left: 130px;
    top: 90px;
    background: var(--card-dark);
  }
  .wordmark {
    display: flex;
    align-items: center;
    gap: 14px;
    font-weight: 900;
    letter-spacing: 2px;
    line-height: 1;
  }
  .wordmark__dot {
    width: 46px;
    height: 46px;
    border-radius: 50%;
  }
  .card--back .wordmark {
    position: absolute;
    left: 168px;
    top: 110px;
    font-size: 86px;
    color: var(--on-dark);
  }
  .card--back .wordmark__dot { background: var(--on-dark); }
  .card--back .web {
    position: absolute;
    left: 0;
    right: 0;
    top: 262px;
    text-align: center;
    font-size: 15px;
    letter-spacing: 5px;
    color: var(--on-dark-soft);
  }
  /* Front of card */
  .card--front {
    left: 450px;
    top: 500px;
    background: var(--paper);
  }
  .card--front .swoosh {
    position: absolute;
    inset: 0;
  }
  .card--front .wordmark {
    position: absolute;
    left: 218px;
    top: 56px;
    font-size: 80px;
    color: var(--ink);
  }
  .card--front .wordmark__dot { background: var(--brand-red); }
  .contact {
    position: absolute;
    left: 34px;
    top: 196px;
    color: var(--on-dark);
  }
  .contact__name {
    margin: 0;
    font-size: 20px;
    font-weight: 500;
  }
  .contact__role {
    margin: 2px 0 12px;
    font-size: 15px;
  }
  .contact__list {
    list-style: none;
    margin: 0;
    padding: 0;
    font-size: 14px;
  }
  .contact__list li {
    display: flex;
    align-items: center;
    gap: 10px;
    margin-bottom: 4px;
  }
  .contact__list svg { width: 13px; height: 13px; fill: var(--on-dark); }
</style>
</head>
<body>

<section class="card card--back" aria-label="Back of business card">
  <div class="wordmark"><span class="wordmark__dot"></span><span>VORN</span></div>
  <div class="web">www.vornelectrical.com.au</div>
</section>

<section class="card card--front" aria-label="Front of business card">
  <svg class="swoosh" viewBox="0 0 620 354" preserveAspectRatio="none" aria-hidden="true">
    <defs>
      <linearGradient id="redBand" x1="0" y1="0" x2="1" y2="1">
        <stop offset="0" stop-color="var(--brand-red)"/>
        <stop offset="1" stop-color="var(--brand-red-deep)"/>
      </linearGradient>
    </defs>
    <path d="M0 150 C 180 200, 420 250, 620 160 L620 354 L0 354 Z" fill="url(#redBand)"/>
    <path d="M150 178 C 330 232, 500 222, 610 150 C 500 236, 320 248, 150 178 Z" fill="var(--ink)"/>
  </svg>

  <div class="wordmark"><span class="wordmark__dot"></span><span>VORN</span></div>

  <div class="contact">
    <p class="contact__name">Liam Carter</p>
    <p class="contact__role">Manager, Commercial Sales</p>
    <ul class="contact__list">
      <li><svg viewBox="0 0 16 16"><path d="M3 1h3l1.5 4-2 1.2a9 9 0 0 0 4.3 4.3l1.2-2 4 1.5v3a2 2 0 0 1-2 2A13 13 0 0 1 1 3a2 2 0 0 1 2-2z"/></svg>555 0142 7780</li>
      <li><svg viewBox="0 0 16 16"><path d="M4 0h8a1 1 0 0 1 1 1v14a1 1 0 0 1-1 1H4a1 1 0 0 1-1-1V1a1 1 0 0 1 1-1zm1 2v10h6V2zm3 11a1 1 0 1 0 0 2 1 1 0 0 0 0-2z"/></svg>555 0198 3164</li>
      <li><svg viewBox="0 0 16 16"><path d="M0 3h16v10H0zm1.5 1.2V12h13V4.2L8 9z"/></svg>liam@vornelectrical.com.au</li>
      <li><svg viewBox="0 0 16 16"><path d="M8 0a8 8 0 1 0 0 16A8 8 0 0 0 8 0zm0 2a6 6 0 0 1 5.7 4H9.5L8 2zm-2 12.6A6 6 0 0 1 2.2 6H5l1 8.6z"/></svg>vornelectrical.com.au</li>
    </ul>
  </div>
</section>

</body>
</html>
```